Greeting Card Design Project

We need a greeting card to email our clients during christmas.

We are suppliers for cutting tools & machine accessories. You can find out more about us at our website www.quvantel.com.sg

Reason: I've decide to extend the deadline as I'm awaiting more designs, thank you.

```html
<!DOCTYPE html>
<html lang="en">
<head>
<meta charset="utf-8">
<title>Quvantel Tools — Christmas Greeting</title>
<link rel="stylesheet" href="https://fonts.googleapis.com/css2?family=Arimo:ital,wght@0,400;1,400&display=swap">
<style>
  :root {
    --paper: #ffffff;
    --panel-light: #c53a2a;
    --panel-mid: #8e1f16;
    --panel-dark: #3b0c07;
    --crimson: #a5182f;
    --ink-soft: #8a8a8a;
  }
  * { margin: 0; padding: 0; box-sizing: border-box; }
  html, body {
    width: 1200px;
    height: 800px;
    overflow: hidden;
    background: var(--paper);
  }
  .greeting-card {
    position: relative;
    width: 1200px;
    height: 800px;
    background: var(--paper);
    font-family: "Arimo", "Helvetica Neue", Arial, sans-serif;
  }
  .tree-panel {
    position: absolute;
    left: 31px;
    top: 0;
    width: 382px;
    height: 800px;
    background:
      radial-gradient(ellipse 70% 45% at 55% 55%, rgba(160, 40, 28, 0.55), transparent 70%),
      linear-gradient(165deg, var(--panel-light) 0%, var(--panel-mid) 40%, var(--panel-dark) 100%);
  }
  .message {
    position: absolute;
    left: 413px;
    right: 0;
    top: 0;
    text-align: center;
  }
  .message__title {
    position: absolute;
    left: 0;
    right: 0;
    top: 300px;
    font-size: 94px;
    font-weight: 400;
    letter-spacing: -0.5px;
    color: var(--crimson);
    line-height: 1;
  }
  .message__thanks {
    position: absolute;
    left: 0;
    right: 0;
    top: 428px;
    font-size: 35px;
    font-style: italic;
    font-weight: 400;
    line-height: 49px;
    color: var(--ink-soft);
  }
  .brand {
    position: absolute;
    right: 40px;
    bottom: 44px;
    display: flex;
    align-items: center;
    gap: 12px;
  }
  .brand__dot {
    width: 30px;
    height: 30px;
    border-radius: 50%;
    background: var(--crimson);
  }
  .brand__name {
    font-size: 30px;
    font-weight: 400;
    color: var(--crimson);
    letter-spacing: 1px;
  }
</style>
</head>
<body>
  <main class="greeting-card">
    <div class="tree-panel" role="img" aria-label="Christmas tree formed by golden sparkles and stars wrapped in a spiralling red ribbon, topped with a shining star"></div>

    <section class="message">
      <h1 class="message__title">Merry Christmas</h1>
      <p class="message__thanks">Thank you for your patronage<br>and loyal business</p>
    </section>

    <div class="brand">
      <span class="brand__dot"></span>
      <span class="brand__name">QUVANTEL TOOLS</span>
    </div>
  </main>
</body>
</html>
```